Glamour By Tavi

I am a makeup artist looking for professional looking double sided business card. I would like to create a logo and incorporate a set of eyes as the periods above the name "Tavi" on the card.

front of card: Logo "Glamour by Tavi" written across diagonal (bottom left to top right)

Back of card:
1) Professional makeup artist serving New York & New Jersey (or similar to this text)
2) 917-555-0148
3) glamourbytavi@mailcove.com

Industry/Entity Type

Business

```html
<!DOCTYPE html>
<html lang="en">
<head>
<meta charset="utf-8">
<title>Glamour by Tavi – Business Cards</title>
<link rel="stylesheet" href="https://fonts.googleapis.com/css2?family=Cinzel:wght@400&family=Open+Sans:ital,wght@0,700;1,700&family=Oswald:wght@300&family=Orbitron:wght@700&display=swap">
<style>
  :root{
    --paper:#ffffff;
    --night:#000000;
    --ink:#4a4a4a;
    --ink-dark:#333333;
    --panel-grey:#686868;
    --header-grey:#6e6e6e;
    --strip-light:#ffffff;
    --strip-dark:#333333;
    --panel-dark:#1e1e1e;
    --card-dark:#1a1a1a;
    --accent:#c0272d;
    --soft:#d9d9d9;
    --white:#ffffff;
  }
  *{margin:0;padding:0;box-sizing:border-box}
  html,body{width:1200px;height:900px;overflow:hidden}
  body{position:relative;background:var(--paper);font-family:"Open Sans",sans-serif}
  .band{position:absolute;left:0;width:1200px}
  .band--light{top:0;height:460px;background:var(--paper)}
  .band--dark{top:460px;height:440px;background:var(--night)}

  .card{position:absolute;width:543px;height:340px;border-radius:12px;overflow:hidden}
  .card--front-light{left:57px;top:70px;border:1px solid #000;background:var(--paper)}
  .card--front-dark{left:57px;top:511px;background:var(--card-dark)}
  .card--back-light{left:624px;top:74px;border:1px solid #000;background:var(--panel-grey)}
  .card--back-dark{left:624px;top:506px;background:var(--panel-dark)}

  /* front */
  .eye-art{position:absolute;top:88px;width:92px;height:52px;border-radius:46px 46px 40px 40px}
  .eye-art--left{left:176px}
  .eye-art--right{left:344px}
  .card--front-light .eye-art{background:linear-gradient(180deg,#7a7a7a 0%,#5c5c5c 55%,#9c9c9c 100%)}
  .card--front-dark .eye-art{background:linear-gradient(180deg,#2e2e2e 0%,#262626 55%,#303030 100%)}
  .wordmark{position:absolute;left:0;width:100%;top:128px;text-align:center;font-family:"Open Sans",sans-serif;font-weight:700;font-size:78px;line-height:84px;letter-spacing:-1px}
  .card--front-light .wordmark{color:var(--ink)}
  .card--front-dark .wordmark{color:#2f2f2f}
  .tagline{position:absolute;left:191px;top:214px;width:203px;font-family:"Cinzel",serif;font-size:10.5px;letter-spacing:.4px;text-transform:uppercase;text-align:center;padding-bottom:3px;border-bottom:2px solid;white-space:nowrap}
  .card--front-light .tagline{color:var(--ink-dark);border-color:#000}
  .card--front-dark .tagline{color:var(--soft);border-color:var(--accent)}
  .corner-name{position:absolute;right:6px;bottom:8px;font-family:"Orbitron",sans-serif;font-weight:700;font-size:8px;letter-spacing:1px;text-transform:uppercase}
  .card--front-light .corner-name{color:#000}
  .card--front-dark .corner-name{color:var(--white)}

  /* back */
  .strip{position:absolute;left:0;top:0;width:222px;height:100%}
  .card--back-light .strip{background:var(--strip-light)}
  .card--back-dark .strip{background:var(--strip-dark);border-right:1px solid #000}
  .eye-column{position:absolute;left:106px;top:10px;width:80px;height:312px}
  .card--back-light .eye-column{background:linear-gradient(90deg,rgba(215,215,215,0),#dcdcdc 30%,#dcdcdc 70%,rgba(215,215,215,0))}
  .card--back-dark .eye-column{background:linear-gradient(90deg,rgba(70,70,70,0),#474747 30%,#474747 70%,rgba(70,70,70,0))}
  .stamp{position:absolute;left:-40px;top:126px;width:200px;height:80px;transform:rotate(-90deg);text-align:center}
  .stamp-name{font-weight:700;font-size:46px;line-height:52px}
  .card--back-light .stamp-name{color:var(--ink)}
  .card--back-dark .stamp-name{color:#1c1c1c}
  .stamp-line{display:inline-block;font-family:"Cinzel",serif;font-size:7px;padding-bottom:2px;border-bottom:1px solid}
  .card--back-light .stamp-line{color:#222;border-color:#000}
  .card--back-dark .stamp-line{color:#111;border-color:var(--accent)}

  .header{position:absolute;left:222px;top:0;width:321px;height:78px}
  .card--back-light .header{background:var(--header-grey);border-bottom:3px solid var(--white)}
  .card--back-dark .header{border-bottom:2px solid var(--accent)}
  .header-eye{position:absolute;left:28px;top:26px;width:86px;height:30px;border-radius:43px 43px 30px 30px}
  .card--back-light .header-eye{background:linear-gradient(180deg,#5a5a5a,#4c4c4c 60%,#626262)}
  .card--back-dark .header-eye{background:linear-gradient(180deg,#333,#2c2c2c 60%,#2a2a2a)}
  .header-title{position:absolute;right:30px;top:12px;font-family:"Oswald",sans-serif;font-weight:300;font-size:50px;line-height:58px;letter-spacing:-.5px}
  .header-by{position:absolute;right:10px;top:20px;height:50px;writing-mode:vertical-rl;transform:rotate(180deg);font-family:"Oswald",sans-serif;font-weight:300;font-size:14px;line-height:16px;text-align:center}
  .card--back-light .header-title,.card--back-light .header-by{color:var(--ink-dark)}
  .card--back-dark .header-title,.card--back-dark .header-by{color:#dddddd}

  .details{position:absolute;left:281px;top:91px;list-style:none}
  .detail{position:relative;margin-bottom:14px}
  .detail::before{content:"";position:absolute;left:-17px;top:5px;width:7px;height:8px;border:1px solid currentColor}
  .detail-label{font-family:"Cinzel",serif;font-size:13px;letter-spacing:.6px;line-height:18px;white-space:nowrap}
  .detail-sub{font-family:"Cinzel",serif;font-size:18px;letter-spacing:1px;line-height:20px;margin-left:21px}
  .detail-value{font-weight:700;font-style:italic;font-size:19px;line-height:26px;margin-left:21px;white-space:nowrap}
  .detail-value--small{font-size:15px;line-height:24px;margin-left:19px}
  .card--back-light .detail,.card--back-light .detail-label{color:var(--white)}
  .card--back-light .detail-sub{color:#111}
  .card--back-light .detail-value{color:var(--white)}
  .card--back-light .detail-value--dark{color:#000}
  .card--back-dark .detail,.card--back-dark .detail-label,.card--back-dark .detail-sub{color:var(--accent)}
  .card--back-dark .detail-value{color:var(--white)}
</style>
</head>
<body>
  <div class="band band--light"></div>
  <div class="band band--dark"></div>

  <section class="card card--front-light">
    <div class="eye-art eye-art--left" role="img" aria-label="Illustrated left eye with brow"></div>
    <div class="eye-art eye-art--right" role="img" aria-label="Illustrated right eye with brow"></div>
    <div class="wordmark">Tavi.</div>
    <div class="tagline">Professional Make Up Artist</div>
    <div class="corner-name">Glamour by Tavi</div>
  </section>

  <section class="card card--back-light">
    <div class="strip">
      <div class="eye-column" role="img" aria-label="Column of faint illustrated eyes"></div>
      <div class="stamp"><div class="stamp-name">Tavi.</div><div class="stamp-line">PROFESSIONAL MAKE UP ARTIST</div></div>
    </div>
    <div class="header">
      <div class="header-eye" role="img" aria-label="Faint illustrated eye"></div>
      <div class="header-title">GLAMOUR</div>
      <div class="header-by">BYTAVI</div>
    </div>
    <ul class="details">
      <li class="detail"><div class="detail-label">PROFESSIONAL MAKE UP ARTIST</div><div class="detail-sub">SERVING:</div><div class="detail-value">NEW YORK</div><div class="detail-value">NEW JERSEY</div></li>
      <li class="detail"><div class="detail-label">CONTACT NUMBER :</div><div class="detail-value detail-value--dark">917-555-0148</div></li>
      <li class="detail"><div class="detail-label">EMAIL ADDRESS :</div><div class="detail-value detail-value--small detail-value--dark">GLAMOURBYTAVI@MAILCOVE.COM</div></li>
    </ul>
  </section>

  <section class="card card--front-dark">
    <div class="eye-art eye-art--left" role="img" aria-label="Illustrated left eye with brow"></div>
    <div class="eye-art eye-art--right" role="img" aria-label="Illustrated right eye with brow"></div>
    <div class="wordmark">Tavi.</div>
    <div class="tagline">Professional Make Up Artist</div>
    <div class="corner-name">Glamour by Tavi</div>
  </section>

  <section class="card card--back-dark">
    <div class="strip">
      <div class="eye-column" role="img" aria-label="Column of faint illustrated eyes"></div>
      <div class="stamp"><div class="stamp-name">Tavi.</div><div class="stamp-line">PROFESSIONAL MAKE UP ARTIST</div></div>
    </div>
    <div class="header">
      <div class="header-eye" role="img" aria-label="Faint illustrated eye"></div>
      <div class="header-title">GLAMOUR</div>
      <div class="header-by">BYTAVI</div>
    </div>
    <ul class="details">
      <li class="detail"><div class="detail-label">PROFESSIONAL MAKE UP ARTIST</div><div class="detail-sub">SERVING:</div><div class="detail-value">NEW YORK</div><div class="detail-value">NEW JERSEY</div></li>
      <li class="detail"><div class="detail-label">CONTACT NUMBER :</div><div class="detail-value">917-555-0148</div></li>
      <li class="detail"><div class="detail-label">EMAIL ADDRESS :</div><div class="detail-value detail-value--small">GLAMOURBYTAVI@MAILCOVE.COM</div></li>
    </ul>
  </section>
</body>
</html>
```